Redesign of Bright Harbor Entertainment Card

I already have my logo and font design for my company name. I am looking to come up with a Unique way of having it on my business card. Just looking for a really hip, and professional business card while still using my logo design.

I have also enclosed the front and back of the card so you can see what I have now. Looking for something different.

Thank you!

Target Market(s)

Young to middle aged brides and grooms

Industry/Entity Type

Business

Requirements
Should not have
• Cheese

```html
<!DOCTYPE html>
<html lang="en">
<head>
<meta charset="utf-8">
<title>Bright Harbor Entertainment – Business Card</title>
<link rel="stylesheet" href="https://fonts.googleapis.com/css2?family=Open+Sans:wght@400;600;800&display=swap">
<style>
  :root {
    --backdrop: #e9e6e2;
    --card: #ffffff;
    --card-shade: #eceef0;
    --ink: #2b2b2b;
    --title-blue: #2a46c8;
    --brand-blue: #3d3fb8;
    --band-blue: #2f3fc4;
    --icon-navy: #1d2c6e;
    --halo: #9fdcf0;
  }
  * { box-sizing: border-box; margin: 0; padding: 0; }
  html, body { width: 1200px; height: 1200px; overflow: hidden; }
  body {
    background: var(--backdrop);
    font-family: "Open Sans", Arial, sans-serif;
    color: var(--ink);
    display: flex;
    flex-direction: column;
    align-items: center;
    justify-content: center;
    gap: 70px;
  }
  .card {
    position: relative;
    width: 770px;
    height: 440px;
    border-radius: 34px;
    background: linear-gradient(160deg, var(--card) 55%, var(--card-shade));
    box-shadow: 0 14px 34px rgba(0,0,0,.22);
    overflow: hidden;
  }
  .brand {
    display: flex;
    align-items: center;
    gap: 18px;
  }
  .brand-dot {
    width: 92px; height: 92px;
    border-radius: 50%;
    background: radial-gradient(circle at 40% 35%, #6fb7f0, var(--brand-blue));
    flex: none;
  }
  .brand-name {
    font-weight: 800;
    font-size: 54px;
    letter-spacing: 2px;
    text-transform: uppercase;
    color: var(--brand-blue);
    line-height: 1;
    white-space: nowrap;
  }

  /* front */
  .card-front .brand { position: absolute; left: 42px; top: 128px; gap: 14px; }
  .card-front .brand-dot { width: 80px; height: 80px; }
  .card-front .brand-name { font-size: 42px; }
  .person { position: absolute; right: 44px; top: 30px; text-align: right; }
  .person-name { font-size: 34px; font-weight: 400; color: #333; line-height: 1.3; }
  .person-role { font-size: 26px; color: var(--title-blue); line-height: 1.3; }
  .watermark-circle {
    position: absolute; right: 44px; top: 190px;
    width: 150px; height: 150px; border-radius: 50%;
    border: 4px solid var(--halo);
    background: rgba(180,190,240,.25);
  }
  .contacts { position: absolute; left: 50px; top: 240px; list-style: none; }
  .contacts li {
    display: flex; align-items: center; gap: 16px;
    font-size: 22px; line-height: 40px; color: #222;
  }
  .contacts svg { width: 24px; height: 24px; flex: none; }
  .band {
    position: absolute; left: 0; right: 0; bottom: 0; height: 18px;
    background: var(--band-blue);
  }

  /* back */
  .card-back .brand { position: absolute; left: 130px; top: 56px; }
  .services { position: absolute; left: 96px; top: 200px; list-style: none; }
  .services li {
    display: flex; align-items: center; gap: 14px;
    font-size: 28px; line-height: 46px; color: #222;
  }
  .services svg { width: 16px; height: 16px; flex: none; }
</style>
</head>
<body>

<section class="card card-front" aria-label="Card front">
  <div class="person">
    <p class="person-name">Dan Whitley</p>
    <p class="person-role">Owner / Emcee</p>
  </div>
  <div class="brand">
    <span class="brand-dot"></span>
    <span class="brand-name">Bright Harbor</span>
  </div>
  <span class="watermark-circle"></span>
  <ul class="contacts">
    <li>
      <svg viewBox="0 0 24 24" aria-hidden="true"><path fill="var(--icon-navy)" d="M6.6 10.8a15.1 15.1 0 0 0 6.6 6.6l2.2-2.2a1 1 0 0 1 1-.25 11.4 11.4 0 0 0 3.6.57 1 1 0 0 1 1 1V20a1 1 0 0 1-1 1A17 17 0 0 1 3 4a1 1 0 0 1 1-1h3.5a1 1 0 0 1 1 1c0 1.25.2 2.45.57 3.57a1 1 0 0 1-.25 1z"/></svg>
      555 014 BEAT (2328)
    </li>
    <li>
      <svg viewBox="0 0 24 24" aria-hidden="true"><rect x="2" y="5" width="20" height="14" rx="1" fill="var(--icon-navy)"/><path d="M2 6l10 7 10-7" stroke="#fff" stroke-width="1.6" fill="none"/></svg>
      info@brightharbor.com
    </li>
    <li>
      <svg viewBox="0 0 24 24" aria-hidden="true"><g fill="none" stroke="var(--icon-navy)" stroke-width="1.8"><circle cx="12" cy="12" r="9.5"/><ellipse cx="12" cy="12" rx="4" ry="9.5"/><path d="M2.5 12h19M4 7h16M4 17h16"/></g></svg>
      www.brightharbor.com
    </li>
    <li>
      <svg viewBox="0 0 24 24" aria-hidden="true"><circle cx="12" cy="12" r="8" fill="var(--icon-navy)"/></svg>
      brightharborentertainment
    </li>
  </ul>
  <div class="band"></div>
</section>

<section class="card card-back" aria-label="Card back">
  <div class="brand">
    <span class="brand-dot"></span>
    <span class="brand-name">Bright Harbor</span>
  </div>
  <ul class="services">
    <li><svg viewBox="0 0 16 16" aria-hidden="true"><path d="M1 1l14 7-14 7z" fill="var(--band-blue)"/></svg>DJs / Emcees</li>
    <li><svg viewBox="0 0 16 16" aria-hidden="true"><path d="M1 1l14 7-14 7z" fill="var(--band-blue)"/></svg>Lighting / Wireless LED Uplighting</li>
    <li><svg viewBox="0 0 16 16" aria-hidden="true"><path d="M1 1l14 7-14 7z" fill="var(--band-blue)"/></svg>Photo Booths</li>
    <li><svg viewBox="0 0 16 16" aria-hidden="true"><path d="M1 1l14 7-14 7z" fill="var(--band-blue)"/></svg>Photo Montages</li>
  </ul>
</section>

</body>
</html>
```